Fielduro home page and search results web design

We are looking for an attractive front page and search page for our website, Fielduro.us. The site is currently up and can be searched. Most of the functionality works, but the design needs to be improved. The website is a platform that allows sports facility managers to list their facilities and allow the public to rent them. Can be thought of as the DineSlot for athletic facilities. The 2 pages we would like designed are the home page, where a renter would search for a facility, and the search results page, where there is a map of the facilities available on the left and the available facility listings on the right.

Target Market(s)

Sports facility managers and sports organizations

Number of Pages Required

2 page

Colors

Designer to choose colors to be used in the design.

Requirements
Must have
• Be very easy for someone visiting the site to use.

```html
<!DOCTYPE html>
<html lang="en">
<head>
<meta charset="utf-8">
<title>Fielduro – Rent a Facility</title>
<link href="https://fonts.googleapis.com/css2?family=Roboto+Condensed:wght@400;700&family=Roboto:wght@400;500&family=Open+Sans:ital,wght@0,400;0,600;1,400&display=swap" rel="stylesheet">
<style>
:root{
  --green:#7cc242;
  --green-dark:#5f9e2c;
  --ink:#2b2b2b;
  --text:#555;
  --muted:#888;
  --light:#f1f1f1;
  --footer:#333333;
  --footer-deep:#2a2a2a;
  --white:#ffffff;
}
*{margin:0;padding:0;box-sizing:border-box}
html,body{width:1200px;height:3180px;overflow:hidden}
body{position:relative;background:var(--white);font-family:"Open Sans",Arial,sans-serif;color:var(--text)}
.abs{position:absolute}
.cond{font-family:"Roboto Condensed","Arial Narrow",sans-serif}

/* header */
.site-header{left:0;top:0;width:1200px;height:96px;background:var(--white);z-index:5;box-shadow:0 1px 4px rgba(0,0,0,.12)}
.brand{left:100px;top:26px;font-family:"Roboto Condensed",sans-serif;font-weight:700;font-size:38px;color:var(--ink);letter-spacing:1px;display:flex;align-items:center;gap:10px}
.brand .dot{width:14px;height:14px;background:var(--green);border-radius:50%}
.main-nav{right:100px;top:0;height:96px;display:flex;align-items:center;gap:30px;font-family:"Roboto",sans-serif;font-size:14px;color:var(--ink)}
.main-nav a{color:var(--ink);text-decoration:none;position:relative}
.main-nav a.active{color:var(--green)}
.main-nav a.active::after{content:"";position:absolute;left:50%;top:58px;margin-left:-8px;border:8px solid transparent;border-top-color:var(--white)}
.login-btn{background:var(--green);color:var(--white)!important;padding:8px 16px;border-radius:3px;display:flex;align-items:center;gap:6px}

/* hero */
.grass{left:0;top:96px;width:1200px;height:1044px;background:linear-gradient(180deg,#5fa52f 0%,#6cb83a 45%,#55982a 100%)}
.stadium{left:0;top:96px;width:1200px;height:594px;clip-path:polygon(0 0,100% 0,100% 86%,50% 100%,0 86%);
  background:linear-gradient(180deg,#7fb0dc 0%,#c8dcee 24%,#e8eef2 36%,#c76a35 48%,#d9804a 64%,#b25a2d 74%,#5e9c34 86%,#4e8a2a 100%)}
.hero-line{left:0;top:590px}
.hero-title{left:0;top:206px;width:1200px;text-align:center;color:var(--white);font-weight:700;font-size:50px;text-shadow:0 2px 6px rgba(0,0,0,.3)}
.hero-lead{left:300px;top:272px;width:600px;text-align:center;color:var(--white);font-size:16px;line-height:27px;text-shadow:0 1px 3px rgba(0,0,0,.45)}
.search-bar{left:212px;top:384px;width:776px;height:56px;background:rgba(20,20,20,.85);padding:8px;display:flex;gap:8px}
.search-field{flex:0 0 214px;background:var(--white);font-family:"Roboto",sans-serif;font-size:12px;color:#777;display:flex;align-items:center;justify-content:space-between;padding:0 14px}
.search-field::after{content:"";border:5px solid transparent;border-top-color:#555;margin-top:5px}
.search-btn{flex:1;background:var(--green);color:var(--white);font-family:"Roboto",sans-serif;font-size:14px;display:flex;align-items:center;justify-content:center}
.slider-dots{left:0;top:622px;width:1200px;display:flex;justify-content:center;gap:8px}
.slider-dots span{width:14px;height:14px;border-radius:50%;border:2px solid var(--white)}
.slider-dots span.on{background:var(--white)}

.why-title{left:0;top:734px;width:1200px;text-align:center;color:var(--white);font-weight:700;font-size:34px}
.feature{width:250px;text-align:center;color:var(--white)}
.feature .icon{width:106px;height:106px;margin:0 auto;border-radius:50%;background:#333;border:3px solid var(--white);display:flex;align-items:center;justify-content:center}
.feature h3{font-family:"Roboto Condensed",sans-serif;font-weight:700;font-size:21px;margin-top:20px}
.feature p{font-size:13.5px;line-height:22px;margin-top:6px}

/* welcome */
.welcome-photo{left:106px;top:1240px;width:436px;height:352px;border:6px solid var(--white);outline:1px solid #999;box-shadow:0 0 0 1px #ccc;background:linear-gradient(135deg,#6f9a4c 0%,#b98a5c 35%,#8fb06a 55%,#c29062 75%,#5d8a3e 100%)}
.welcome-title{left:606px;top:1272px;font-size:34px;color:var(--ink);font-weight:400}
.welcome-copy{left:606px;top:1332px;width:494px;font-size:11.5px;line-height:22px;color:var(--text)}
.welcome-copy p+p{margin-top:14px}
.btn{background:var(--green);color:var(--white);font-family:"Roboto",sans-serif;font-weight:500;font-size:13px;display:flex;align-items:center;justify-content:center}
.learn-btn{left:606px;top:1518px;width:116px;height:32px}

/* featured */
.featured{left:0;top:1685px;width:1200px;height:590px;background:linear-gradient(180deg,#f4f4f4,#ebebeb)}
.section-title{left:0;width:1200px;text-align:center;font-size:34px;color:var(--ink)}
.card{top:1834px;width:233px;height:308px;background:var(--white);border-radius:4px;box-shadow:0 1px 4px rgba(0,0,0,.25);overflow:hidden}
.card .photo{height:190px}
.card svg{position:absolute;left:0;top:150px}
.card .price{position:absolute;top:213px;width:100%;text-align:center;font-family:"Roboto",sans-serif;font-size:19px;color:var(--ink)}
.card .place{position:absolute;top:248px;width:100%;text-align:center;font-family:"Roboto",sans-serif;font-size:13.5px;line-height:20px;color:var(--ink)}
.view-btn{left:548px;top:2192px;width:104px;height:30px}

/* community */
.community{left:0;top:2275px;width:1200px;height:540px;background:linear-gradient(180deg,#ffffff,#f3f3f3)}
.community-sub{left:0;top:2400px;width:1200px;text-align:center;font-family:"Roboto",sans-serif;font-size:14px;color:var(--ink)}
.testimonial{top:2488px;width:340px;display:flex;gap:20px}
.avatar{flex:0 0 76px;height:76px;border-radius:50%;border:3px solid #ddd;background:linear-gradient(180deg,#d9d3cc,#b9aea3)}
.quote{font-style:italic;font-size:11.5px;line-height:20px;color:var(--text);position:relative;padding-left:16px}
.quote::before{content:"\201C";position:absolute;left:0;top:-6px;font-size:28px;color:var(--green);font-style:normal;font-family:Georgia,serif}
.quote .who{display:block;font-style:normal;color:var(--green);margin-top:8px}
.com-dots{left:0;top:2660px;width:1200px;display:flex;justify-content:center;gap:8px;align-items:center}
.com-dots span{width:12px;height:12px;border-radius:50%;background:var(--ink)}
.com-dots span.on{width:16px;height:16px;background:var(--white);border:3px solid var(--green)}

/* footer */
.footer-shape{left:0;top:2750px}
.footer-brand{left:0;top:2802px;width:1200px;display:flex;justify-content:center;align-items:center;gap:10px;font-family:"Roboto Condensed",sans-serif;font-weight:700;font-size:36px;color:var(--white)}
.footer-brand .dot{width:13px;height:13px;background:var(--green);border-radius:50%}
.f-col{top:2876px}
.f-col h4{font-family:"Roboto Condensed",sans-serif;font-weight:400;font-size:19px;color:var(--green);margin-bottom:22px}
.f-contact li{list-style:none;display:flex;gap:14px;font-size:12.5px;line-height:20px;color:#ddd;margin-bottom:14px}
.f-contact svg{flex:0 0 14px;margin-top:3px}
.f-news p{font-size:12.5px;line-height:20px;color:#ddd;width:250px}
.email-box{margin-top:16px;width:246px;height:42px;background:var(--white);font-family:"Roboto",sans-serif;font-size:12px;color:#666;display:flex;align-items:center;padding:0 12px}
.sub-btn{margin-top:16px;width:122px;height:40px}
.f-links li{list-style:none;font-family:"Roboto",sans-serif;font-size:12px;color:#ddd;line-height:22px;display:flex;align-items:center;gap:10px}
.f-links li::before{content:"";border:4px solid transparent;border-left-color:#ddd;border-right:0}
.f-social li{list-style:none;display:flex;align-items:center;gap:12px;font-family:"Roboto",sans-serif;font-size:14px;color:#ddd;margin-bottom:12px}
.f-social li span{width:28px;height:28px;border-radius:50%;border:1.5px solid #ddd}
.copyright{left:0;top:3116px;width:1200px;height:64px;background:var(--footer-deep);border-top:1px solid #444;text-align:center;font-family:"Roboto",sans-serif;font-size:12px;color:#ccc;line-height:64px}
</style>
</head>
<body>

<header class="site-header abs">
  <div class="brand abs">Fielduro <span class="dot"></span></div>
  <nav class="main-nav abs">
    <a class="active" href="#">HOME</a>
    <a href="#">SEARCH</a>
    <a href="#">RENTERS</a>
    <a href="#">FACILITY MANAGER</a>
    <a href="#">SUBSCRIPTION</a>
    <a class="login-btn" href="#">
      <svg width="11" height="12" viewBox="0 0 11 12"><circle cx="5.5" cy="3.5" r="3" fill="#fff"/><path d="M0 12c0-3.5 2.5-5 5.5-5s5.5 1.5 5.5 5z" fill="#fff"/></svg>LOGIN</a>
  </nav>
</header>

<section class="hero">
  <div class="grass abs" role="img" aria-label="Close view of a freshly mown grass pitch"></div>
  <div class="stadium abs" role="img" aria-label="Open stadium with orange seating under a blue cloudy sky"></div>
  <svg class="hero-line abs" width="1200" height="110" viewBox="0 0 1200 110">
    <polyline points="0,11 600,100 1200,11" fill="none" stroke="#fff" stroke-width="4"/>
  </svg>
  <h1 class="hero-title abs cond">RENT A FACILITY</h1>
  <p class="hero-lead abs">Reserv a facility that suits you, for your practicies, tournamnets and events. Never struggle to find facilities for your practices, book in advance for a nominal price.</p>
  <div class="search-bar abs">
    <div class="search-field">City</div>
    <div class="search-field">State</div>
    <div class="search-field">Zipcode</div>
    <div class="search-btn">SEARCH</div>
  </div>
  <div class="slider-dots abs"><span class="on"></span><span></span><span></span><span></span></div>

  <h2 class="why-title abs cond">WHY CHOOSE US?</h2>
  <div class="feature abs" style="left:79px;top:820px">
    <div class="icon"><svg width="48" height="48" viewBox="0 0 48 48" fill="none" stroke="#fff" stroke-width="5"><path d="M38 18a15 15 0 0 0-27-4"/><path d="M10 30a15 15 0 0 0 27 4"/><path d="M40 8v11H29" stroke-linejoin="round"/><path d="M8 40V29h11" stroke-linejoin="round"/></svg></div>
    <h3>HOW IT WORKS</h3>
    <p>Fielduro is an online platform and marketplace for people to list, discover, and book facilities for sports activities.</p>
  </div>
  <div class="feature abs" style="left:344px;top:820px">
    <div class="icon"><svg width="50" height="50" viewBox="0 0 50 50"><path d="M6 6h18l20 20-18 18L6 24z" fill="#fff"/><circle cx="15" cy="15" r="4" fill="#333"/></svg></div>
    <h3>RENTERS</h3>
    <p>Renters can browse listings and filter by location, type of facility, or keyword. Once users find a facility they like</p>
  </div>
  <div class="feature abs" style="left:609px;top:820px">
    <div class="icon"><svg width="52" height="44" viewBox="0 0 52 44" fill="#fff"><circle cx="26" cy="10" r="8"/><path d="M12 40c0-10 6-15 14-15s14 5 14 15z"/><circle cx="9" cy="15" r="6"/><path d="M0 38c0-7 4-11 9-11 2 0 3 .5 4 1-3 3-4 6-4 10z"/><circle cx="43" cy="15" r="6"/><path d="M52 38c0-7-4-11-9-11-2 0-3 .5-4 1 3 3 4 6 4 10z"/></svg></div>
    <h3>OWNERS</h3>
    <p>Fielduro owners add facility information, location, pictures, availability, pricing When an renter reservs a facility</p>
  </div>
  <div class="feature abs" style="left:874px;top:820px">
    <div class="icon"><svg width="38" height="48" viewBox="0 0 38 48"><path d="M2 2h22l12 12v32H2z" fill="#fff"/><path d="M24 2v12h12" fill="#ccc"/><g stroke="#333" stroke-width="3"><path d="M9 24h20M9 31h20M9 38h20"/></g></svg></div>
    <h3>BENEFITS</h3>
    <p>Manage your facilities online and earn more income. Fielduro will handle back end details to guarantee a safe</p>
  </div>
</section>

<section class="welcome">
  <div class="welcome-photo abs" role="img" aria-label="Aerial view of a baseball park complex with several diamonds"></div>
  <h2 class="welcome-title abs cond">WELCOME TO FIELDURO</h2>
  <div class="welcome-copy abs">
    <p>Sed ut perspiciatis unde omnis iste natus error sit voluptatem accusantium doloremque laudantium, totam rem aperiam, eaque ipsa quae ab illo inventore veritatis et quasi architecto beatae vitae dicta sunt explicabo. Nemo enim ipsam voluptatem quia voluptas sit aspernatur aut odit aut fugit, sed quia consequuntur magni dolores eos.</p>
    <p>Sed ut perspiciatis unde omnis iste natus error sit voluptatem accusantium doloremque laudantium, totam rem aperiam, eaque ipsa quae ab illo inventore veritatis et quasi architecto beatae vitae dicta sunt explicabo. Nemo enim ipsam voluptatem quia voluptas.</p>
  </div>
  <div class="learn-btn btn abs">LEARN MORE</div>
</section>

<section class="featured abs"></section>
<h2 class="section-title abs cond" style="top:1744px">FEATURED FACILITIES</h2>

<article class="card abs" style="left:100px">
  <div class="photo" role="img" aria-label="Indoor turf field with running track" style="background:linear-gradient(180deg,#6e7a84,#9aa3a8 40%,#5f8f4a 70%,#4b7a3b)"></div>
  <svg width="233" height="60" viewBox="0 0 233 60"><path d="M0 10Q116 70 233 10V60H0z" fill="#fff"/><path d="M0 10Q116 70 233 10" fill="none" stroke="#7cc242" stroke-width="3"/></svg>
  <div class="price">$50 per hour</div>
  <div class="place">Indoor Soccer Field Cedarvale,<br>TX, 75090</div>
</article>
<article class="card abs" style="left:355px">
  <div class="photo" role="img" aria-label="Indoor gym with hardwood basketball court" style="background:linear-gradient(180deg,#8a7d6a,#b9a78a 45%,#a9906b 70%,#8f7a5a)"></div>
  <svg width="233" height="60" viewBox="0 0 233 60"><path d="M0 10Q116 70 233 10V60H0z" fill="#fff"/><path d="M0 10Q116 70 233 10" fill="none" stroke="#7cc242" stroke-width="3"/></svg>
  <div class="price">$60 per hour</div>
  <div class="place">Indoor Soccer Field Cedarvale,<br>TX, 75090</div>
</article>
<article class="card abs" style="left:610px">
  <div class="photo" role="img" aria-label="Large indoor arena with green turf under lights" style="background:linear-gradient(180deg,#2f3a2c,#4d6a3a 45%,#3f7a2e 75%,#2f6224)"></div>
  <svg width="233" height="60" viewBox="0 0 233 60"><path d="M0 10Q116 70 233 10V60H0z" fill="#fff"/><path d="M0 10Q116 70 233 10" fill="none" stroke="#7cc242" stroke-width="3"/></svg>
  <div class="price">$80 per hour</div>
  <div class="place">Indoor Soccer Field Cedarvale,<br>TX, 75090</div>
</article>
<article class="card abs" style="left:865px">
  <div class="photo" role="img" aria-label="Indoor volleyball courts in blue and red" style="background:linear-gradient(180deg,#7a5a4a,#c0563a 45%,#3a6fb0 70%,#c65a3c)"></div>
  <svg width="233" height="60" viewBox="0 0 233 60"><path d="M0 10Q116 70 233 10V60H0z" fill="#fff"/><path d="M0 10Q116 70 233 10" fill="none" stroke="#7cc242" stroke-width="3"/></svg>
  <div class="price">$20 per hour</div>
  <div class="place">Indoor Soccer Field Cedarvale,<br>TX, 75090</div>
</article>
<div class="view-btn btn abs">VIEW MORE</div>

<section class="community abs"></section>
<h2 class="section-title abs cond" style="top:2352px">MEET OUR COMMUNITY</h2>
<p class="community-sub abs">See what people are saying about Fielduro.</p>

<div class="testimonial abs" style="left:98px">
  <div class="avatar" role="img" aria-label="Portrait photo of a community member"></div>
  <p class="quote">At vero eos et accusamus et iusto odio dignissimos ducimus qui blanditiis praesentium voluptatum deleniti atque corrupti dolores et quas molestias.<span class="who">Facility Manager - Marcus Hale</span></p>
</div>
<div class="testimonial abs" style="left:448px">
  <div class="avatar" role="img" aria-label="Portrait photo of a community member"></div>
  <p class="quote">At vero eos et accusamus et iusto odio dignissimos ducimus qui blanditiis praesentium voluptatum deleniti atque corrupti dolores et quas molestias.<span class="who">Renter - Dean Porter</span></p>
</div>
<div class="testimonial abs" style="left:804px">
  <div class="avatar" role="img" aria-label="Portrait photo of a community member"></div>
  <p class="quote">At vero eos et accusamus et iusto odio dignissimos ducimus qui blanditiis praesentium voluptatum deleniti atque corrupti dolores et quas molestias.<span class="who">Facility Owner - Owen Barrett</span></p>
</div>
<div class="com-dots abs"><span class="on"></span><span></span><span></span><span></span></div>

<footer>
  <svg class="footer-shape abs" width="1200" height="366" viewBox="0 0 1200 366">
    <path d="M0 70L600 8L1200 70V366H0z" fill="#333"/>
    <path d="M0 70L600 8L1200 70" fill="none" stroke="#7cc242" stroke-width="6"/>
  </svg>
  <div class="footer-brand abs">Fielduro <span class="dot"></span></div>

  <div class="f-col f-contact abs" style="left:98px">
    <h4>CONTACT US</h4>
    <ul>
      <li><svg width="14" height="16" viewBox="0 0 14 16"><path d="M7 0a6 6 0 0 0-6 6c0 4.5 6 10 6 10s6-5.5 6-10a6 6 0 0 0-6-6z" fill="#ddd"/><circle cx="7" cy="6" r="2.2" fill="#333"/></svg>218 Fielduro Way, Suite 40 Maple Grove CA<br>90000</li>
      <li><svg width="14" height="14" viewBox="0 0 14 14"><path d="M3 0l3 3-2 2c1 2 3 4 5 5l2-2 3 3-2 3C6 14 0 8 0 3z" fill="#ddd"/></svg>Phone: (555) 014-2290</li>
      <li><svg width="14" height="12" viewBox="0 0 14 12"><rect y="1" width="14" height="10" fill="#ddd"/><path d="M0 1l7 5 7-5" fill="none" stroke="#333" stroke-width="1.5"/></svg>Email: info@fielduro.us</li>
    </ul>
  </div>

  <div class="f-col f-news abs" style="left:456px">
    <h4>SIGN UP FOR NEWSLETTER</h4>
    <p>Excepteur sint occaecat cupidatat non proident, sunt in culpa qui officia deserunt</p>
    <div class="email-box">Enter email</div>
    <div class="sub-btn btn">SUBSCRIPTION</div>
  </div>

  <div class="f-col f-links abs" style="left:798px">
    <h4>QUICK LINKS</h4>
    <ul>
      <li>Home</li><li>Search</li><li>Renters</li><li>Facility Manager</li><li>Subscription</li><li>Login</li><li>Contact Us</li>
    </ul>
  </div>

  <div class="f-col f-social abs" style="left:1003px">
    <h4>SOCIAL</h4>
    <ul>
      <li><span></span>Facelink</li>
      <li><span></span>Chirper</li>
      <li><span></span>Searchly+</li>
      <li><span></span>Vidstream</li>
    </ul>
  </div>

  <div class="copyright abs">Copyright © 2017 Fielduro. All rights reserved.</div>
</footer>

</body>
</html>
```